Hybrid education and entertainment company needs help with creating dynamic school worksheets

I'm looking for a skilled individual to create a versatile Microsoft Word template for school worksheets for Lessonvaria. Your task will involve:
- Designing a user-friendly and visually appealing template that can be easily customized for various subjects and grade levels.
- Ensuring the template includes sections for titles, instructions, questions, and space for student responses.
- Incorporating consistent formatting and styles to maintain a professional look across all worksheets.
- Adding placeholders for images, graphics, or interactive elements to enhance engagement.
- Testing the template to ensure compatibility and ease of use for educators.
Your work will help streamline the worksheet creation process, making it easier for educators to develop effective and engaging learning materials.

```html
<!DOCTYPE html>
<html lang="en">
<head>
<meta charset="utf-8">
<title>Lessonvaria Worksheet Template</title>
<link href="https://fonts.googleapis.com/css2?family=Poppins:wght@400;500;600;700;800&display=swap" rel="stylesheet">
<style>
  :root {
    --brand-blue: #22ace3;
    --ink: #111111;
    --paper: #ffffff;
    --backdrop: #e6e7e9;
  }
  * { margin: 0; padding: 0; box-sizing: border-box; }
  html, body {
    width: 1000px;
    height: 1200px;
    overflow: hidden;
    background: var(--backdrop);
    font-family: "Poppins", sans-serif;
  }
  .worksheet {
    position: absolute;
    left: 76px;
    top: 0;
    width: 848px;
    height: 1200px;
    background: var(--paper);
  }
  .worksheet > * { position: absolute; }
  .centered-y { transform: translateY(-50%); }

  .logo-box {
    left: 110px; top: 102px;
    width: 221px; height: 63px;
    border: 3px solid var(--brand-blue);
    display: flex; align-items: center; justify-content: center;
    color: var(--brand-blue);
    font-weight: 700; font-size: 29px; letter-spacing: -0.3px;
  }

  .meta-field {
    left: 569px;
    font-size: 20px; color: var(--ink);
    display: flex; align-items: baseline; gap: 4px;
  }
  .meta-field .fill-dots {
    border-bottom: 2px dotted var(--ink);
    height: 1px;
  }
  .meta-date { top: 173px; }
  .meta-date .fill-dots { width: 117px; }
  .meta-grade { top: 207px; }
  .meta-grade .fill-dots { width: 102px; }

  .worksheet-title {
    left: 0; width: 100%; top: 312px;
    text-align: center;
    color: var(--brand-blue);
    font-weight: 700; font-size: 75px; letter-spacing: 0.5px;
    line-height: 1;
  }

  .section-heading {
    left: 108px;
    color: var(--brand-blue);
    font-weight: 700; font-size: 33px;
    line-height: 1;
  }
  .heading-instructions { top: 413px; }
  .heading-questions { top: 537px; }
  .heading-long-answer { top: 841px; }

  .instructions-text {
    left: 108px; top: 464px;
    font-size: 23.5px; color: var(--ink);
    white-space: nowrap;
  }

  .question-item {
    left: 108px;
    font-size: 15.5px; color: var(--ink);
    white-space: nowrap;
  }
  .question-item .q-num { display: inline-block; width: 26px; }
  .q1 { top: 606px; }
  .q2 { top: 660px; }
  .q3 { top: 713px; }
  .q4 { top: 769px; }

  .image-placeholder {
    left: 505px; top: 536px;
    width: 240px; height: 247px;
    border: 3px solid var(--brand-blue);
    color: var(--brand-blue);
    font-weight: 700; font-size: 31px;
    text-align: center;
  }
  .image-placeholder span {
    position: absolute; left: 0; width: 100%;
    transform: translateY(-50%);
    line-height: 1;
  }
  .image-placeholder .line-one { top: 87px; }
  .image-placeholder .line-two { top: 142px; }

  .answer-line {
    left: 108px; width: 641px;
    height: 2px; background: var(--ink);
  }
  .answer-line-1 { top: 908px; }
  .answer-line-2 { top: 954px; }
  .answer-line-3 { top: 1000px; }

  .tagline {
    left: 0; width: 100%; top: 1060px;
    text-align: center;
    color: var(--brand-blue);
    font-size: 26.5px; font-weight: 400;
  }

  .page-number {
    right: 99px; top: 1114px;
    font-size: 23px; color: var(--ink);
  }
</style>
</head>
<body>
  <main class="worksheet">
    <div class="logo-box">LOGO PLACE</div>

    <div class="meta-field meta-date centered-y">Date <span class="fill-dots"></span></div>
    <div class="meta-field meta-grade centered-y">Grade <span class="fill-dots"></span></div>

    <h1 class="worksheet-title centered-y">WORKSHEET TITLE</h1>

    <h2 class="section-heading heading-instructions centered-y">Instructions:</h2>
    <p class="instructions-text centered-y">Lorem ipsum dolor sit amet, consectetur adipiscing elit,</p>

    <h2 class="section-heading heading-questions centered-y">Questions</h2>
    <p class="question-item q1 centered-y"><span class="q-num">1.</span>Lorem ipsum dolor sit amet, consectetur ?</p>
    <p class="question-item q2 centered-y"><span class="q-num">2.</span>Lorem ipsum dolor sit amet, consectetur ?</p>
    <p class="question-item q3 centered-y"><span class="q-num">3.</span>Lorem ipsum dolor sit amet, consectetur ?</p>
    <p class="question-item q4 centered-y"><span class="q-num">4.</span>Lorem ipsum dolor sit amet, consectetur ?</p>

    <div class="image-placeholder">
      <span class="line-one">Insert</span>
      <span class="line-two">IMAGE HERE</span>
    </div>

    <h2 class="section-heading heading-long-answer centered-y">Long Answer</h2>
    <div class="answer-line answer-line-1"></div>
    <div class="answer-line answer-line-2"></div>
    <div class="answer-line answer-line-3"></div>

    <p class="tagline centered-y">Engaging Learning Materials for All Grades</p>
    <p class="page-number centered-y">01</p>
  </main>
</body>
</html>
```